Tidal Fern Business Cards

We need something new, fun and exciting for business cards. Our current ones are just plain and we need a design that pops. We want name, position held, phone, email on the front, and a 20% discount on the back. I have also uploaded our old business cards creative to see what we are not wanting, and how boring they were and we want something jazzed up from this, cool design and catches people attention.

```html
<!DOCTYPE html>
<html lang="en">
<head>
<meta charset="utf-8">
<title>Tidal Fern Business Cards</title>
<link rel="stylesheet" href="https://fonts.googleapis.com/css2?family=Montserrat:wght@600;700;800&family=Arimo:wght@400;700&display=swap">
<style>
  :root {
    --navy: #1b3f72;
    --salmon: #f07370;
    --red: #dc1d3a;
    --white: #ffffff;
    --ink: #1a1a1a;
    --rule: #555b66;
    --stage: #232323;
  }
  * { margin: 0; padding: 0; box-sizing: border-box; }
  html, body { width: 1200px; height: 1015px; overflow: hidden; }
  body {
    background: var(--stage);
    position: relative;
    font-family: "Arimo", Arial, sans-serif;
  }
  .card {
    position: absolute;
    width: 560px;
    height: 320px;
    overflow: hidden;
  }

  /* Back card */
  .card-back {
    left: 60px; top: 110px;
    background: var(--navy);
  }
  .card-back .brand {
    position: absolute;
    left: 0; right: 0; top: 70px;
    display: flex; align-items: center; justify-content: center; gap: 16px;
  }
  .brand-dot {
    width: 30px; height: 30px; border-radius: 50%;
    background: var(--salmon);
  }
  .brand-name {
    font-family: "Montserrat", sans-serif;
    font-weight: 700;
    font-size: 50px;
    letter-spacing: -0.5px;
  }
  .card-back .brand-name { color: var(--white); }
  .offer-band {
    position: absolute;
    left: 0; right: 0; top: 182px; height: 28px;
    background: var(--salmon);
  }
  .offer-badge {
    position: absolute;
    left: 50%; top: 196px;
    width: 112px; height: 112px;
    margin: -56px 0 0 -56px;
    border-radius: 50%;
    background: var(--red);
    box-shadow: 0 0 0 8px var(--navy);
    display: flex; flex-direction: column; align-items: center; justify-content: center;
    color: var(--white);
    font-family: "Montserrat", sans-serif;
    font-weight: 800;
    line-height: 1;
  }
  .offer-value { font-size: 36px; }
  .offer-label { font-size: 12px; letter-spacing: 0.5px; margin-top: 3px; }

  /* Front card */
  .card-front {
    left: 580px; top: 585px;
    background: var(--white);
  }
  .card-front .brand {
    position: absolute;
    left: 30px; top: 88px; width: 230px;
    display: flex; flex-direction: column; align-items: center; gap: 12px;
  }
  .card-front .brand-dot { width: 36px; height: 36px; }
  .card-front .brand-name { color: var(--navy); font-size: 44px; }
  .divider {
    position: absolute;
    left: 282px; top: 40px;
    width: 1px; height: 190px;
    background: var(--rule);
  }
  .contact {
    position: absolute;
    left: 302px; top: 44px;
    color: var(--ink);
  }
  .person-name {
    font-family: "Montserrat", sans-serif;
    font-weight: 800;
    font-size: 24px;
    color: var(--navy);
    line-height: 1.05;
  }
  .person-role { font-size: 14px; margin-bottom: 12px; }
  .contact-list { list-style: none; font-size: 14px; line-height: 1.45; }
  .contact-list li { display: flex; align-items: center; gap: 8px; }
  .contact-list svg { width: 15px; height: 15px; flex: none; fill: var(--navy); }
  .web-accent { color: var(--salmon); }
  .address { font-size: 14px; line-height: 1.35; margin: 10px 0 0 23px; }
  .footer-navy {
    position: absolute;
    left: 0; bottom: 0; width: 345px; height: 18px;
    background: var(--navy);
  }
  .footer-salmon {
    position: absolute;
    right: 0; bottom: 0; width: 212px; height: 30px;
    background: var(--salmon);
  }
</style>
</head>
<body>

<section class="card card-back" aria-label="Business card back">
  <div class="brand">
    <span class="brand-dot"></span>
    <span class="brand-name">Tidal Fern</span>
  </div>
  <div class="offer-band"></div>
  <div class="offer-badge">
    <span class="offer-value">20%</span>
    <span class="offer-label">DISCOUNT</span>
  </div>
</section>

<section class="card card-front" aria-label="Business card front">
  <div class="brand">
    <span class="brand-dot"></span>
    <span class="brand-name">Tidal Fern</span>
  </div>
  <div class="divider"></div>
  <div class="contact">
    <p class="person-name">Marcus Hale</p>
    <p class="person-role">Managing Director</p>
    <ul class="contact-list">
      <li>
        <svg viewBox="0 0 24 24" aria-hidden="true"><path d="M6.6 10.8a15.1 15.1 0 0 0 6.6 6.6l2.2-2.2a1 1 0 0 1 1-.25 11.4 11.4 0 0 0 3.6.57 1 1 0 0 1 1 1V20a1 1 0 0 1-1 1A17 17 0 0 1 3 4a1 1 0 0 1 1-1h3.5a1 1 0 0 1 1 1c0 1.25.2 2.45.57 3.57a1 1 0 0 1-.25 1z"/></svg>
        044-987 654 321
      </li>
      <li>
        <svg viewBox="0 0 24 24" aria-hidden="true"><path d="M2 5h20v14H2z M2 5l10 8 10-8" fill="none" stroke="#1b3f72" stroke-width="2"/></svg>
        hello@tidalfernmail.com
      </li>
      <li>
        <svg viewBox="0 0 24 24" aria-hidden="true"><g fill="none" stroke="#1b3f72" stroke-width="2"><circle cx="12" cy="12" r="9"/><ellipse cx="12" cy="12" rx="4" ry="9"/><path d="M3 12h18M5 7h14M5 17h14"/></g></svg>
        <span>www.<span class="web-accent">tidalfern</span>.com</span>
      </li>
    </ul>
    <p class="address">88, Harbour Lane<br>Bayview Coast, 31807</p>
  </div>
  <div class="footer-navy"></div>
  <div class="footer-salmon"></div>
</section>

</body>
</html>
```